Cash Back to Home Buyers Flyer

We need a flyer for Brisk Haven real estate brokerage advertising Money Saving Offer to Home buyers - Cash Back Rebate and explaining how the concept works. The design should communicate how that money saving offer works and should motivate buyers to take advantage of it. Feel free to edit the text based on the attached designs and use infographics.

Target Market(s)

Middle aged professionals

Industry/Entity Type

Real Estate

Requirements
Must have
• Call to action highlights, Dollar signs. Graphics to show rebate math as in the attached file.

```html
<!DOCTYPE html>
<html lang="en">
<head>
<meta charset="utf-8">
<title>Brisk Haven – Home Buyers Rebate Flyer</title>
<link href="https://fonts.googleapis.com/css2?family=Arimo:wght@700&family=Lato:wght@400;700&family=Montserrat:wght@600;700&display=swap" rel="stylesheet">
<style>
  :root {
    --teal: #12b5a1;
    --teal-dark: #0e9c8b;
    --band-gray: #868686;
    --backdrop: #3b3b3b;
    --ink: #1c1c1c;
    --white: #ffffff;
    --line: #555555;
  }
  * { margin: 0; padding: 0; box-sizing: border-box; }
  html, body { width: 1200px; height: 1200px; overflow: hidden; background: var(--backdrop); }
  .flyer {
    position: absolute; left: 246px; top: 94px; width: 718px; height: 1008px;
    background: var(--white); overflow: hidden;
  }
  .hero { position: absolute; left: 0; top: 0; width: 718px; height: 424px; }
  .brand {
    position: absolute; left: 60px; top: 96px; display: flex; align-items: center; gap: 10px;
    font-family: "Lato", sans-serif; font-weight: 700; font-size: 30px; color: var(--teal);
  }
  .brand-square { width: 16px; height: 16px; background: var(--teal); }
  .headline {
    position: absolute; left: 24px; top: 184px; width: 340px;
    font-family: "Arimo", sans-serif; font-weight: 700; font-size: 32px; line-height: 35px; color: var(--white);
  }
  .hero-copy {
    position: absolute; left: 26px; top: 306px; width: 372px;
    font-family: "Lato", sans-serif; font-size: 16px; line-height: 20px; color: var(--white);
  }
  .promise-band {
    position: absolute; left: 0; top: 432px; width: 718px; height: 177px; background: var(--band-gray);
  }
  .promise-title {
    position: absolute; left: 50px; top: 60px;
    font-family: "Arimo", sans-serif; font-weight: 700; font-size: 30px; line-height: 33px; color: var(--white);
  }
  .promise-divider { position: absolute; left: 344px; top: 32px; width: 16px; height: 128px; }
  .promise-copy {
    position: absolute; left: 377px; top: 48px; width: 308px;
    font-family: "Lato", sans-serif; font-size: 14px; line-height: 17px; color: var(--white);
  }
  .benefit { position: absolute; top: 679px; width: 200px; height: 148px; border: 1.2px solid var(--line); }
  .benefit-icon { position: absolute; left: 50%; top: -48px; width: 96px; height: 96px; margin-left: -48px; }
  .benefit-text {
    position: absolute; left: 16px; top: 65px; white-space: nowrap;
    font-family: "Montserrat", sans-serif; font-weight: 600; font-size: 14.5px; line-height: 20px;
    letter-spacing: -0.2px; color: var(--ink);
  }
  .benefit-text.centered { left: 0; right: 0; top: 73px; text-align: center; }
  .benefit--rebate { left: 35px; }
  .benefit--cost { left: 262px; }
  .benefit--amount { left: 485px; }
  .how-it-works {
    position: absolute; left: 46px; top: 851px; width: 640px;
    font-family: "Lato", sans-serif; font-size: 13.6px; line-height: 17px; color: var(--ink);
  }
  .disclaimer {
    position: absolute; left: 41px; top: 918px; width: 650px;
    font-family: "Montserrat", sans-serif; font-weight: 600; font-size: 12.4px; color: var(--ink); letter-spacing: -0.1px;
  }
  .contact-bar {
    position: absolute; left: 0; top: 947px; width: 718px; height: 61px; background: var(--teal);
    display: flex; align-items: center; justify-content: space-between; padding: 0 48px 10px 42px;
    font-family: "Lato", sans-serif; font-weight: 700; font-size: 16px; color: var(--white);
  }
</style>
</head>
<body>
<main class="flyer">
  <svg class="hero" viewBox="0 0 718 424">
    <defs>
      <linearGradient id="houseTones" x1="0" y1="0" x2="0.3" y2="1">
        <stop offset="0" stop-color="#8fa6c9"/>
        <stop offset="0.45" stop-color="#c9c8cf"/>
        <stop offset="0.62" stop-color="#d99a52"/>
        <stop offset="0.82" stop-color="#6f86ad"/>
        <stop offset="1" stop-color="#3f6a3a"/>
      </linearGradient>
    </defs>
    <polygon role="img" aria-label="Photo of a large stone house at dusk with a lit arched doorway and wide front steps" points="286,0 718,0 718,424 466,424" fill="url(#houseTones)"/>
    <polygon points="0,168 357,168 458,406 0,406" fill="var(--teal)"/>
  </svg>

  <div class="brand"><span class="brand-square"></span>Brisk Haven</div>

  <h1 class="headline">Home Buyers Rebate up to 2% of Home Selling Price</h1>
  <p class="hero-copy">We share our Commission with Home Buyers ! Up to 2% Cash Back towards Buyer's Closing Costs. Get thousands of dollars from your agent's commission at closing !</p>

  <section class="promise-band">
    <h2 class="promise-title">WE SELL HOMES<br>FASTER FOR LESS!</h2>
    <svg class="promise-divider" viewBox="0 0 16 128">
      <line x1="2" y1="0" x2="2" y2="128" stroke="#ffffff" stroke-width="2"/>
      <polygon points="2,54 14,61 2,68" fill="#ffffff"/>
    </svg>
    <p class="promise-copy">We charge LESS to sell your home. The typical total commission is 5%-6% split between the agents. Instead of charging 2.5% or 3% as a Listing agent, we charge only 1-1.5%. And with us you are always in control !</p>
  </section>

  <div class="benefit benefit--rebate">
    <svg class="benefit-icon" viewBox="0 0 96 96">
      <circle cx="48" cy="48" r="47" fill="#fff" stroke="#333" stroke-width="1.5" stroke-dasharray="1.5 2"/>
      <circle cx="48" cy="48" r="42" fill="var(--teal)"/>
      <text x="48" y="64" text-anchor="middle" font-family="Arimo, sans-serif" font-weight="700" font-size="50" fill="#fff">$</text>
      <polygon points="40,70 56,70 48,82" fill="#fff"/>
    </svg>
    <p class="benefit-text">You can get up to 2%<br>of Selling price back in<br>your pocket at closing</p>
  </div>

  <div class="benefit benefit--cost">
    <svg class="benefit-icon" viewBox="0 0 96 96">
      <circle cx="48" cy="48" r="47" fill="#fff" stroke="#333" stroke-width="1.5" stroke-dasharray="1.5 2"/>
      <circle cx="48" cy="48" r="42" fill="var(--teal)"/>
      <path d="M36 42 L46 34 M41 34 H46 V39 M52 40 L66 26 M58 26 H66 V34" stroke="#fff" stroke-width="4" fill="none"/>
      <text x="48" y="66" text-anchor="middle" font-family="Montserrat, sans-serif" font-weight="700" font-size="22" fill="#fff">COST</text>
    </svg>
    <p class="benefit-text centered">Average rebate we<br>payfor a $500,000</p>
  </div>

  <div class="benefit benefit--amount">
    <svg class="benefit-icon" viewBox="0 0 96 96">
      <circle cx="48" cy="48" r="47" fill="#fff" stroke="#333" stroke-width="1.5" stroke-dasharray="1.5 2"/>
      <circle cx="48" cy="48" r="42" fill="var(--teal)"/>
      <circle cx="48" cy="48" r="26" fill="none" stroke="#fff" stroke-width="8" stroke-dasharray="7 6"/>
      <circle cx="48" cy="48" r="21" fill="#fff"/>
      <text x="48" y="61" text-anchor="middle" font-family="Arimo, sans-serif" font-weight="700" font-size="36" fill="var(--teal)">$</text>
    </svg>
    <p class="benefit-text centered">Home sale is about<br>$7,500 !</p>
  </div>

  <p class="how-it-works">Working with us is not much different from working with a traditional Realtor. You simply start your home search online and we handle everything else. The same great level of service, professional advice and guidance PLUS a huge check at your closing to cover your closing costs !</p>
  <p class="disclaimer">All commissions are negotiable in NJ. Consult a tax professional regarding a receipt of the rebate.</p>

  <footer class="contact-bar">
    <span>(555) 014-2290</span><span>|</span><span>info@briskhaven.net</span><span>|</span><span>www.briskhaven.net</span>
  </footer>
</main>
</body>
</html>
```